BRQW Coaching Website

I would like someone to design my website. I have an existing site which is really basic and needs an overhaul. I have attached a powerpoint with all the information I require. I am flexible with the design and layout and am ok with graphics being added to enhance the attractiveness of the site.

```html
<!DOCTYPE html>
<html lang="en">
<head>
<meta charset="utf-8">
<title>BRQW Coaching</title>
<link rel="stylesheet" href="https://fonts.googleapis.com/css2?family=Abel&family=Arimo&display=swap">
<style>
:root{
  --navy:#0e3a63;
  --orange:#ff6a0d;
  --orange-text:#f0773a;
  --brand-blue:#1b6fb5;
  --band-grey:#b3b3b3;
  --panel-grey:#efefef;
  --line:#dcdcdc;
  --text-grey:#a9a9a9;
  --dark:#2b2b2b;
  --darker:#3d3d3d;
  --white:#ffffff;
}
*{box-sizing:border-box;margin:0;padding:0}
html,body{width:941px;height:1200px;overflow:hidden;background:var(--white)}
body{position:relative;font-family:"Abel",sans-serif;color:#333}
.abs{position:absolute}

/* header */
.brand{left:86px;top:30px;font-size:24px;color:var(--brand-blue);letter-spacing:.5px}
.contact-line{left:643px;font-size:15px;color:var(--navy);display:flex;align-items:center;gap:10px}
.contact-line svg{width:17px;height:14px;fill:var(--navy)}
.social{top:62px;left:803px;display:flex;gap:4px}
.social span{width:14px;height:14px;display:block}

/* nav */
.nav{left:0;top:93px;width:941px;height:36px;background:var(--navy)}
.nav a{position:absolute;top:0;height:36px;line-height:36px;font-size:11px;color:var(--white);text-decoration:none;text-transform:uppercase}
.nav .active{left:87px;width:78px;background:var(--orange);text-align:center}

/* hero */
.hero{left:88px;top:139px;width:767px;height:279px;border:1px solid var(--line);background:#fbfbfb;box-shadow:0 6px 6px -4px rgba(0,0,0,.15);overflow:hidden}
.hero-brand{left:48px;top:30px;width:221px;height:96px;background:var(--white);display:flex;align-items:center;justify-content:center;font-size:28px;color:var(--brand-blue)}
.hero-accent{left:0;top:160px;width:767px;height:30px;background:linear-gradient(180deg,rgba(255,106,13,.28),rgba(14,58,99,.28))}
.hero-photo{left:342px;top:30px;width:410px;height:215px;background:radial-gradient(ellipse at center,#d8c3b2 0%,#c9cfd6 60%,#f6f6f6 100%)}
.hero-list{left:16px;top:197px;list-style:none;font-size:11px;color:var(--orange-text);text-transform:uppercase;line-height:13.8px;letter-spacing:.7px}
.hero-list li::before{content:"›";display:inline-block;width:12px;font-weight:bold;color:var(--orange)}
.hero-note{left:502px;top:261px;font-size:10.5px;color:var(--orange-text);letter-spacing:.2px}

/* welcome */
.welcome{left:0;top:433px;width:941px;height:104px;background:var(--band-grey);color:var(--white);font-size:15px;line-height:18px;text-align:center;padding-top:25px}

/* cards */
.card{top:554px;width:182px;height:190px;border:1px solid var(--line);background:var(--white);text-align:center}
.card h2{font-weight:normal;font-size:17px;color:var(--orange-text);text-transform:uppercase;margin-top:8px;letter-spacing:.3px}
.card .pic{width:142px;height:142px;border-radius:50%;border:3px solid #ececec;margin:7px auto 0}

/* cta */
.cta{left:88px;top:755px;width:767px;height:83px;background:var(--panel-grey)}
.cta p{position:absolute;left:70px;top:29px;font-size:20.5px;color:var(--navy)}
.cta .btn{position:absolute;left:585px;top:18px;width:139px;height:47px;background:var(--white);border:1px solid var(--line);font-size:18px;color:var(--navy);text-align:center;line-height:45px}

/* about */
.about{left:88px;top:852px;width:377px;height:225px;border:1px solid var(--line)}
.portrait{left:11px;top:11px;width:116px;height:164px;background:linear-gradient(160deg,#9aa58a,#5a4c44 60%,#e59a8c)}
.bio{left:141px;top:12px;width:230px;font-size:15px;line-height:18.2px;color:var(--text-grey)}
.btn-navy{background:var(--navy);color:var(--white);text-align:center;font-size:15px;text-transform:uppercase}

/* form */
.form{left:478px;top:852px;width:377px;height:225px;border:1px solid var(--line);font-family:"Arimo",sans-serif}
.form label{position:absolute;left:12px;font-size:12px;color:#333}
.form .field{position:absolute;left:12px;width:355px;background:var(--panel-grey);border:1px solid #cfcfcf;font-size:12px;font-style:italic;color:#aaa;padding:3px 4px}

/* footer */
.footer{left:0;top:1090px;width:941px;height:85px;background:var(--dark);border-top:3px solid #e6e6e6}
.footer ul{position:absolute;top:12px;list-style:none;font-size:9px;line-height:16px;color:#9a9a9a;text-transform:uppercase;font-family:"Arimo",sans-serif}
.footer .divider{position:absolute;top:13px;width:1px;height:58px;background:#555}
.footer-brand{left:398px;top:18px;font-size:20px;color:#8a8a8a}
.footer-contact{left:609px;font-size:9px;color:#9a9a9a;font-family:"Arimo",sans-serif;display:flex;gap:8px;align-items:center}
.footer-contact svg{width:12px;height:10px;fill:#9a9a9a}
.footer-social{left:610px;top:46px;display:flex;gap:3px}
.footer-social span{width:17px;height:17px;display:block}
.legal{left:0;top:1175px;width:941px;height:25px;background:var(--darker);color:#aaa;font-size:9px;line-height:25px;text-align:center;font-family:"Arimo",sans-serif}
</style>
</head>
<body>

<header>
  <div class="abs brand">BRQW Coaching</div>
  <div class="abs contact-line" style="top:15px">
    <svg viewBox="0 0 17 14"><path d="M1 4c3-4 12-4 15 0l-2 2-3-1V3H6v2L3 6z M4 8h9l2 5H2z"/></svg>1300 555 017
  </div>
  <div class="abs contact-line" style="top:36px">
    <svg viewBox="0 0 17 14"><path d="M0 2h17v10H0z M0 2l8.5 6L17 2" stroke="#fff" stroke-width="1"/></svg>maren.oakes@brqwcoaching.com
  </div>
  <div class="abs social"><span style="background:#1f6ea6"></span><span style="background:#2a9fd6"></span><span style="background:#d9533e"></span></div>
</header>

<nav class="abs nav">
  <a class="active" href="#">Home</a>
  <a href="#" style="left:192px">Individual Coaching &#9662;</a>
  <a href="#" style="left:347px">Group Work</a>
  <a href="#" style="left:457px">Resources &#9662;</a>
  <a href="#" style="left:572px">Inspiration Booth</a>
  <a href="#" style="left:708px">About</a>
  <a href="#" style="left:789px">Contact</a>
</nav>

<section class="abs hero">
  <div class="abs hero-accent" role="img" aria-label="Decorative orange and navy wave band"></div>
  <div class="abs hero-photo" role="img" aria-label="Group of cheering people with raised arms"></div>
  <div class="abs hero-brand">BRQW Coaching</div>
  <ul class="abs hero-list">
    <li>Growth &amp; Professional Development</li>
    <li>Managing Your Time</li>
    <li>Career Advancement &amp; Goal Setting</li>
    <li>Speaking With Confidence</li>
    <li>Effective Leadership</li>
  </ul>
  <p class="abs hero-note">Get your free 30 minute introductory coaching session</p>
</section>

<section class="abs welcome">
  Welcome to BRQW Coaching where we put a new perspective on the way you work, live and play.<br>
  Through our programs you will learn new skills &amp; techniques to enable you to break through the barriers that have kept you from<br>
  reaching your full potential up to now.
</section>

<article class="abs card" style="left:88px"><h2>Individual Coaching</h2><div class="pic" role="img" aria-label="Smiling woman in a white blouse" style="background:radial-gradient(circle,#e8ddd0,#f4f4f4)"></div></article>
<article class="abs card" style="left:283px"><h2>Group Work</h2><div class="pic" role="img" aria-label="Colleagues discussing at a table" style="background:radial-gradient(circle,#9fc3d8,#e4eef3)"></div></article>
<article class="abs card" style="left:478px"><h2>Resources</h2><div class="pic" role="img" aria-label="Professionals from different trades standing together" style="background:radial-gradient(circle,#5a4a44,#d4d8dc)"></div></article>
<article class="abs card" style="left:673px"><h2>Inspiration Booth</h2><div class="pic" role="img" aria-label="Woman with arms raised in a golden field" style="background:radial-gradient(circle,#e2c58a,#f1ece2)"></div></article>

<section class="abs cta">
  <p>Get your free 30 minute introductory coaching session</p>
  <div class="btn">CLICK HERE</div>
</section>

<section class="abs about">
  <div class="abs portrait" role="img" aria-label="Portrait of the coach"></div>
  <p class="abs bio">Maren Oakes is a full time working Mum who believes that life is what you make it. She has experience in a variety of industries including Banking &amp; Finance, Telecommunications, Hospitality, Manufacturing and Farming. Maren spent three years working abroad in England, Scotland, Spain and Canada.</p>
  <div class="abs btn-navy" style="left:274px;top:184px;width:90px;height:31px;line-height:31px">More</div>
</section>

<section class="abs form">
  <label style="top:14px">Name:</label>
  <div class="field" style="top:27px;height:21px">Enter Name</div>
  <label style="top:56px">Email:</label>
  <div class="field" style="top:69px;height:21px">Enter Email</div>
  <label style="top:98px">Message:</label>
  <div class="field" style="top:111px;height:58px">Enter Your Message</div>
  <div class="abs btn-navy" style="left:275px;top:183px;width:92px;height:32px;line-height:32px;font-family:'Abel',sans-serif">Send</div>
</section>

<footer class="abs footer">
  <ul style="left:87px"><li>Home</li><li>Individual Coaching</li><li>Group Work</li><li>Resources</li></ul>
  <ul style="left:199px"><li>Inspiration Booth</li><li>About</li><li>Contact</li></ul>
  <span class="divider" style="left:339px"></span>
  <div class="abs footer-brand">BRQW Coaching</div>
  <span class="divider" style="left:601px"></span>
  <div class="abs footer-contact" style="top:12px"><svg viewBox="0 0 17 14"><path d="M1 4c3-4 12-4 15 0l-2 2-3-1V3H6v2L3 6z M4 8h9l2 5H2z"/></svg>1300 555 017</div>
  <div class="abs footer-contact" style="top:28px"><svg viewBox="0 0 17 14"><path d="M0 2h17v10H0z"/></svg>maren.oakes@brqwcoaching.com</div>
  <div class="abs footer-social"><span style="background:#1f6ea6"></span><span style="background:#2a9fd6"></span><span style="background:#d9533e"></span></div>
</footer>
<div class="abs legal">© 2014 Bright Road Quiet Wins Coaching. All Rights Reserved.</div>

</body>
</html>
```